Preoperative Medical clearance for Patients on blood thinners

Prepare a flow chart which directs medical office staff to properly triage patients preparing for surgery who are on blood thinners. We will provide a rudimentary flow chart with all necessary information. We need a better layout which is more appealing and intuitive.

Target Market(s)

internal office use

Industry/Entity Type

Medical

Font styles to use
Sans Serif

Requirements
Must have
• attractive, intuitive layout
Should not have
• things that promote confusion

```html
<!DOCTYPE html>
<html lang="en">
<head>
<meta charset="utf-8">
<title>Preoperative Medical Clearance for Patients on Blood Thinners</title>
<link href="https://fonts.googleapis.com/css2?family=Open+Sans:wght@600;700;800&display=swap" rel="stylesheet">
<style>
  :root{
    --node:#fdbe16;
    --ink:#231f20;
    --yes:#f26522;
    --no:#8b1a3a;
    --flow:#231f20;
    --end:#4db8e8;
    --rule:#555555;
    --bg:#ffffff;
  }
  html,body{margin:0;padding:0;overflow:hidden;background:var(--bg);}
  .chart{position:relative;width:1200px;height:907px;overflow:hidden;background:var(--bg);font-family:"Open Sans",Arial,sans-serif;color:var(--ink);}
  .chart-title{position:absolute;left:0;top:18px;width:1200px;margin:0;text-align:center;font-size:35px;font-weight:700;letter-spacing:-0.2px;}
  .title-rule{position:absolute;left:0;top:72px;width:1200px;height:2px;background:var(--rule);}
  .connectors{position:absolute;left:0;top:0;}
  .node{position:absolute;box-sizing:border-box;background:var(--node);border-radius:20px;display:flex;align-items:center;padding:0 22px;font-size:14.5px;font-weight:700;line-height:1.35;}
  .node.center{justify-content:center;text-align:center;}
  .label{position:absolute;font-weight:700;line-height:1;}
  .label.yes{color:var(--yes);font-size:28px;}
  .label.no{color:var(--no);font-size:28px;}
  .label.branch{color:var(--flow);font-size:19px;}
  .label.branch.vertical{transform:rotate(-90deg);transform-origin:left top;}
  .end{position:absolute;left:550px;top:118px;color:var(--end);font-size:36px;font-weight:800;}
</style>
</head>
<body>
<main class="chart">
  <h1 class="chart-title">Preoperative Medical clearance for Patients on blood thinners</h1>
  <div class="title-rule"></div>

  <svg class="connectors" width="1200" height="907" viewBox="0 0 1200 907" aria-hidden="true">
    <defs>
      <marker id="head-yes" viewBox="0 0 10 10" refX="8" refY="5" markerWidth="4.5" markerHeight="4.5" orient="auto"><path d="M0 0L10 5L0 10z" fill="#f26522"/></marker>
      <marker id="head-no" viewBox="0 0 10 10" refX="8" refY="5" markerWidth="4.5" markerHeight="4.5" orient="auto"><path d="M0 0L10 5L0 10z" fill="#8b1a3a"/></marker>
      <marker id="head-flow" viewBox="0 0 10 10" refX="8" refY="5" markerWidth="4.5" markerHeight="4.5" orient="auto"><path d="M0 0L10 5L0 10z" fill="#231f20"/></marker>
    </defs>
    <g fill="none" stroke-width="4">
      <path d="M425 140H538" stroke="#8b1a3a" marker-end="url(#head-no)"/>
      <path d="M275 168V240" stroke="#f26522" marker-end="url(#head-yes)"/>
      <path d="M147 275H102V437H180" stroke="#231f20" marker-end="url(#head-flow)"/>
      <path d="M437 292H686V380" stroke="#231f20" marker-end="url(#head-flow)"/>
      <path d="M437 263H981V380" stroke="#231f20" marker-end="url(#head-flow)"/>
      <path d="M275 465V530" stroke="#f26522" marker-end="url(#head-yes)"/>
      <path d="M378 432H427V617" stroke="#8b1a3a" marker-end="url(#head-no)"/>
      <path d="M597 405H549V617" stroke="#8b1a3a" marker-end="url(#head-no)"/>
      <path d="M686 442V515" stroke="#f26522" marker-end="url(#head-yes)"/>
      <path d="M985 442V515" stroke="#f26522" marker-end="url(#head-yes)"/>
      <path d="M1104 410H1134V655H645" stroke="#8b1a3a" marker-end="url(#head-no)"/>
      <path d="M1134 410V530" stroke="#8b1a3a" marker-end="url(#head-no)"/>
      <path d="M372 674L337 698" stroke="#f26522" marker-end="url(#head-yes)"/>
      <path d="M534 684V742" stroke="#8b1a3a" marker-end="url(#head-no)"/>
      <path d="M230 764V797" stroke="#231f20" marker-end="url(#head-flow)"/>
    </g>
  </svg>

  <div class="node center" style="left:157px;top:113px;width:263px;height:52px;">Patient taking a blood thinner?</div>
  <div class="node" style="left:147px;top:252px;width:290px;height:61px;">Cardiac problem, bleeding disorder, or stroke?</div>
  <div class="node center" style="left:190px;top:413px;width:188px;height:47px;">Have a cardiologist?</div>
  <div class="node" style="left:165px;top:538px;width:237px;height:56px;">Refer to Patient’s current cardiologist?</div>
  <div class="node center" style="left:597px;top:391px;width:186px;height:47px;">Have a neurologist?</div>
  <div class="node center" style="left:586px;top:527px;width:220px;height:52px;">Refer to neurologist</div>
  <div class="node center" style="left:872px;top:391px;width:232px;height:47px;">Have a hematologist?</div>
  <div class="node" style="left:873px;top:527px;width:228px;height:60px;padding-left:38px;">Refe to hematologist for clearance</div>
  <div class="node center" style="left:378px;top:628px;width:250px;height:52px;">Have a primary care doctor?</div>
  <div class="node" style="left:115px;top:709px;width:240px;height:52px;">Call primary and ask for preferred cardiologist.</div>
  <div class="node center" style="left:65px;top:805px;width:337px;height:47px;">Refer to cardiologist selected by primary</div>
  <div class="node center" style="left:464px;top:751px;width:338px;height:51px;">Select specialist and refer to establish care</div>

  <div class="end">END</div>

  <span class="label no" style="left:450px;top:108px;">No</span>
  <span class="label yes" style="left:290px;top:178px;">Yes</span>
  <span class="label branch vertical" style="left:70px;top:405px;">CARDIAC</span>
  <span class="label branch" style="left:538px;top:268px;">STROKE</span>
  <span class="label branch" style="left:775px;top:234px;">Bleeding disorder</span>
  <span class="label yes" style="left:284px;top:477px;">Yes</span>
  <span class="label no" style="left:432px;top:489px;">No</span>
  <span class="label no" style="left:499px;top:534px;">No</span>
  <span class="label yes" style="left:697px;top:455px;">Yes</span>
  <span class="label yes" style="left:997px;top:460px;">Yes</span>
  <span class="label no" style="left:1083px;top:477px;">No</span>
  <span class="label no" style="left:660px;top:662px;">No</span>
  <span class="label yes" style="left:358px;top:685px;">Yes</span>
  <span class="label no" style="left:540px;top:696px;">No</span>
</main>
</body>
</html>
```